Fundbolt Informational Banners for Ember Hollow Drift

Hello, We are currently in the Process of doing a Fundbolt Campaign which is due on the 4th. We need a Grungy/Dirty Dark Dead Feeling set of Banners, and Informational Pieces in Various Sizes.
Banner Sizes:
640px × 88px Normall Banner
640px × 57px Breaker Banner
700px × 93px Header Banner
640px × 635px Display Box for Rewards
A Larger box, that needs to have a Seamless beginning and ending also needs to be made, so it can be extended as more text and so-forth is completed.

We are looking for very Dead, Dark looking images, thesr are ment to be displayed on the fundbolt webpage they need to flow well with the fundbolt form, as well as show off our things, simple or advanced. They need to match our style.

NOTE IMPORTANT!!!!
THESE ARE NOT ADVERTISING BANNERS, THESE ARE BANNERS FOR THE FUNDBOLT WEBSITE FOR A CAMPAIGN PLEASE DO SOME HOMEWORK BEFORE ATTEMPTING THESE IMAGES WE ARE NOT LOOKING FOR ADVERTISING BANNERS WE ARE LOOKING FOR INFORMATIONAL PIECES

Example of words that will be used on the various Banners

"Physical Add-ons"
"Digital Add-ons"
"Who we are"
"What is Ember Hollow Drift?"
"What is Procedural Generation?"
"Why are you Attempting this?"

THESE ARE EXAMPLE SENTENCES THAT WILL BE IN THE BANNERS I REPEAT THESE ARE NOT ADVERTISING WEBBANNERS
Updates

Everyone is Doing wonderful, thank you all for making such lovely work. thank You. Keep it up, remember undead feel, it must be functional piece on the fundbolt website. :3 

Target Market(s)

Zombie, and Undead ages People 13-51 that are Gamers

Industry/Entity Type

Digital

Requirements
Must have
• These Designs must be Boxes and Banners, and Break Points for a Fundbolt Information Display I will provide a few links here.
http://www.fundbolt.example/projects/quarvex/lament-shores-of-veldrith
http://www.fundbolt.example/projects/brindlework/venture-solace

Our Artwork Style & Concept Artwork can be found here
http://www.gamevault-plaza.example/games/ember-hollow-drift/images

```html
<!DOCTYPE html>
<html lang="en">
<head>
<meta charset="utf-8">
<title>Ember Hollow Drift — Physical Add-ons</title>
<link rel="stylesheet" href="https://fonts.googleapis.com/css2?family=Arimo:wght@400&display=swap">
<style>
  :root {
    --canvas-black: #0b0606;
    --ember-deep: #3a0a06;
    --ember-mid: #7a1a0c;
    --ember-hot: #c8401c;
    --smoke: #1c1412;
    --title-red: #ff1f1f;
    --title-shadow: rgba(0, 0, 0, 0.85);
  }

  html, body {
    margin: 0;
    padding: 0;
    width: 1200px;
    height: 165px;
    overflow: hidden;
    background: var(--canvas-black);
  }

  .section-banner {
    position: relative;
    width: 1200px;
    height: 165px;
    overflow: hidden;
    background: var(--canvas-black);
  }

  .section-banner__artwork {
    position: absolute;
    inset: 0;
    background:
      radial-gradient(ellipse 220px 140px at 90px 40px, var(--ember-hot) 0%, var(--ember-mid) 35%, transparent 75%),
      radial-gradient(ellipse 260px 120px at 230px 150px, var(--ember-mid) 0%, var(--ember-deep) 45%, transparent 80%),
      radial-gradient(ellipse 200px 160px at 1130px 90px, var(--ember-mid) 0%, var(--ember-deep) 45%, transparent 80%),
      radial-gradient(ellipse 180px 90px at 880px 150px, var(--ember-deep) 0%, transparent 80%),
      radial-gradient(ellipse 300px 120px at 560px 40px, var(--smoke) 0%, transparent 80%),
      linear-gradient(90deg, var(--ember-deep) 0%, var(--canvas-black) 40%, var(--smoke) 60%, var(--canvas-black) 80%, var(--ember-deep) 100%);
  }

  .section-banner__title {
    position: absolute;
    left: 98px;
    top: 62px;
    margin: 0;
    font-family: "Arimo", Arial, sans-serif;
    font-weight: 400;
    font-size: 41px;
    line-height: 1;
    letter-spacing: 0;
    color: var(--title-red);
    text-shadow: 1px 1px 2px var(--title-shadow);
    white-space: nowrap;
  }
</style>
</head>
<body>
  <header class="section-banner">
    <div class="section-banner__artwork" role="img" aria-label="Dark grungy fiery game artwork with glowing red embers and shadowy undead figures"></div>
    <h1 class="section-banner__title">Physical Add-ons</h1>
  </header>
</body>
</html>
```